Professional Modern Website Design

We are a premium IT services provider to the financial industry based in London. Our company is called Veltra our current holding page is www.veltra-example.co.uk. We require a new website to match our new corporate identity. This project is for the design phase only. Development will be handled in-house. I have attached examples of wire frames we have developed (although open to suggestions for improvement) Our brand document that should demonstrate current brand, inc how we communicate to potential clients and finally mostly completed web-content.
We are looking for designers that can create something that sets us apart from our competitors.
Target Market(s)
IT Decision makers in Finance companies such as; hedge funds, private investment banks etc
Industry/Entity Type
Financial
Number of Pages Required
5+ page
Requirements
Must have
- hexagon elements in the design, unique design.
Nice to have
- Blog and social media feeds
Should not have
- Should not resemble a downloaded template

```html
<!DOCTYPE html>
<html lang="en">
<head>
<meta charset="utf-8">
<title>Veltra — Premium IT Services for Finance</title>
<link rel="stylesheet" href="https://fonts.googleapis.com/css2?family=Arimo:wght@400;700&display=swap">
<style>
  :root {
    --orange: #f47e20;
    --orange-deep: #e8561a;
    --orange-hex: #e95c18;
    --orange-hex-rim: #f39445;
    --orange-soft: #f9b97f;
    --white: #ffffff;
    --ink: #1a1a1a;
    --nav-grey: #8a8a8a;
    --footer: #5b5b5b;
    --awards-light: #e6e6e6;
    --awards-mid: #cfcfcf;
  }
  * { margin: 0; padding: 0; box-sizing: border-box; }
  html, body { width: 1200px; height: 3028px; overflow: hidden; }
  body {
    position: relative;
    background: var(--white);
    font-family: "Arimo", Helvetica, Arial, sans-serif;
    color: var(--ink);
  }
  .abs { position: absolute; }

  /* Header */
  .site-header { position: absolute; left: 0; top: 0; width: 1200px; height: 77px; background: var(--white); z-index: 5; }
  .brand-tab { position: absolute; left: 61px; top: 0; width: 126px; height: 157px; z-index: 6; }
  .brand-name {
    position: absolute; left: 0; top: 88px; width: 126px; text-align: center;
    font-size: 17px; letter-spacing: 4px; color: var(--orange-deep); font-weight: 400;
  }
  .main-nav a {
    position: absolute; top: 30px; font-size: 14px; color: var(--nav-grey);
    text-decoration: none; letter-spacing: 0.3px;
  }
  .main-nav a.is-current { color: var(--orange-deep); }

  /* Hero */
  .hero-photo {
    position: absolute; left: 0; top: 77px; width: 1200px; height: 748px;
    background:
      radial-gradient(ellipse at 70% 20%, rgba(255,150,60,0.55), transparent 55%),
      linear-gradient(180deg, #e8603a 0%, #c8582e 18%, #4a2a22 40%, #2a1c18 65%, #3a2217 100%);
    clip-path: polygon(0 0, 100% 0, 100% 651px, 50% 745px, 0 651px);
  }
  .hero-banner { position: absolute; left: 169px; top: 466px; width: 864px; height: 183px; }
  .hero-title {
    position: absolute; left: 0; top: 490px; width: 1200px; text-align: center;
    font-size: 41px; color: var(--white); font-weight: 400;
  }
  .hero-lead {
    position: absolute; left: 246px; top: 548px; width: 708px; text-align: center;
    font-size: 15px; line-height: 23px; color: var(--white);
  }

  /* Values */
  .values-band { position: absolute; left: 0; top: 700px; width: 1200px; height: 770px; }
  .value { position: absolute; top: 905px; width: 340px; text-align: center; color: var(--white); }
  .value-hex { display: block; margin: 0 auto; width: 178px; height: 196px; }
  .value-title { margin-top: 44px; font-size: 24px; font-weight: 700; letter-spacing: 0.5px; }
  .value-text { margin-top: 22px; font-size: 15px; line-height: 23px; }

  /* People */
  .section-title {
    position: absolute; left: 0; width: 1200px; text-align: center;
    font-size: 36px; font-weight: 400; letter-spacing: 0.5px;
  }
  .people-title { top: 1532px; color: var(--ink); }
  .portrait { position: absolute; left: 73px; top: 1623px; width: 360px; height: 413px; }
  .person-name { position: absolute; left: 496px; top: 1712px; font-size: 24px; font-weight: 400; }
  .person-role { position: absolute; left: 496px; top: 1746px; font-size: 17px; }
  .person-bio { position: absolute; left: 496px; top: 1795px; width: 620px; font-size: 13.5px; line-height: 22px; }

  /* Awards */
  .awards-band {
    position: absolute; left: 0; top: 2095px; width: 1200px; height: 640px;
    background: radial-gradient(ellipse at 50% 45%, var(--awards-light) 0%, var(--awards-mid) 100%);
    clip-path: polygon(0 0, 50% 92px, 100% 0, 100% 100%, 0 100%);
  }
  .trophy {
    position: absolute; left: 990px; top: 2248px; width: 210px; height: 390px;
    background: linear-gradient(90deg, #2a2a2a 0%, #9a9a9a 35%, #e8e8e8 50%, #6a6a6a 70%, #1e1e1e 100%);
    border-radius: 40px 0 0 0;
  }
  .awards-title { top: 2252px; color: var(--white); }
  .award { position: absolute; top: 2363px; width: 180px; height: 202px; }

  /* Footer */
  .site-footer {
    position: absolute; left: 0; top: 2638px; width: 1200px; height: 390px;
    background: var(--footer);
    clip-path: polygon(0 0, 50% 92px, 100% 0, 100% 100%, 0 100%);
  }
  .copyright {
    position: absolute; left: 0; top: 2809px; width: 1200px; text-align: center;
    font-size: 13px; font-weight: 700; color: var(--white);
  }
  .social-link { position: absolute; top: 2854px; width: 16px; height: 16px; border-radius: 50%; background: var(--white); }
  .back-to-top { position: absolute; left: 588px; top: 2925px; width: 24px; height: 16px; }
</style>
</head>
<body>

<header class="site-header">
  <nav class="main-nav">
    <a class="is-current" href="#" style="left:533px">HOME</a>
    <a href="#" style="left:626px">ABOUT</a>
    <a href="#" style="left:724px">SERVICES</a>
    <a href="#" style="left:844px">PARTNERS</a>
    <a href="#" style="left:966px">CLIENTS</a>
    <a href="#" style="left:1076px">CONTACT</a>
  </nav>
</header>

<div class="brand-tab">
  <svg width="126" height="157" viewBox="0 0 126 157">
    <polygon points="0,0 126,0 126,118 63,157 0,118" fill="#ffffff"/>
  </svg>
  <div class="brand-name">VELTRA</div>
</div>

<div class="hero-photo" role="img" aria-label="City skyline at sunset with lit office towers"></div>
<svg class="abs" style="left:0;top:724px" width="1200" height="110" viewBox="0 0 1200 110">
  <polygon points="0,4 600,98 1200,4 1200,16 600,110 0,16" fill="var(--orange-deep)"/>
</svg>

<svg class="hero-banner" viewBox="0 0 864 183">
  <polygon points="40,0 824,0 864,91 824,183 40,183 0,91" fill="rgba(150,70,10,0.72)"/>
</svg>
<h1 class="hero-title">BRAND DOCUMENT</h1>
<p class="hero-lead">Veltra is one of the leading systems integrators to the world’s finance sector, with more than 40 years’ experience working with the highest-profile financial organisations to build a solid foundation for mutual growth.</p>

<svg class="values-band" viewBox="0 0 1200 770">
  <polygon points="0,28 600,120 1200,28 1200,674 600,765 0,674" fill="var(--orange)"/>
</svg>

<section class="values">
  <div class="value" style="left:68px">
    <svg class="value-hex" viewBox="0 0 178 196" role="img" aria-label="Handshake icon">
      <polygon points="89,0 178,49 178,147 89,196 0,147 0,49" fill="var(--orange-hex-rim)"/>
      <polygon points="89,12 167,55 167,141 89,184 11,141 11,55" fill="var(--orange-hex)"/>
    </svg>
    <h2 class="value-title">COMMITMENT</h2>
    <p class="value-text">Ut enim ad minim veniam, quis nostrud exercitation ullamco laboris nisi ut aliquip ex ea commodo consequat. Duis aute irure dolor in reprehenderit in voluptate velit</p>
  </div>
  <div class="value" style="left:428px">
    <svg class="value-hex" viewBox="0 0 178 196" role="img" aria-label="Leaping figure icon">
      <polygon points="89,0 178,49 178,147 89,196 0,147 0,49" fill="var(--orange-hex-rim)"/>
      <polygon points="89,12 167,55 167,141 89,184 11,141 11,55" fill="var(--orange-hex)"/>
    </svg>
    <h2 class="value-title">DYNAMISM</h2>
    <p class="value-text">Ut enim ad minim veniam, quis nostrud exercitation ullamco laboris nisi ut aliquip ex ea commodo consequat. Duis aute irure dolor in reprehenderit in voluptate velit</p>
  </div>
  <div class="value" style="left:788px">
    <svg class="value-hex" viewBox="0 0 178 196" role="img" aria-label="Running figure icon">
      <polygon points="89,0 178,49 178,147 89,196 0,147 0,49" fill="var(--orange-hex-rim)"/>
      <polygon points="89,12 167,55 167,141 89,184 11,141 11,55" fill="var(--orange-hex)"/>
    </svg>
    <h2 class="value-title">AGILITY</h2>
    <p class="value-text">Ut enim ad minim veniam, quis nostrud exercitation ullamco laboris nisi ut aliquip ex ea commodo consequat. Duis aute irure dolor in reprehenderit in voluptate velit</p>
  </div>
</section>

<h2 class="section-title people-title">OUR PEOPLE</h2>
<svg class="portrait" viewBox="0 0 360 413">
  <polygon points="180,0 360,103 360,310 180,413 0,310 0,103" fill="var(--orange-soft)"/>
  <defs>
    <linearGradient id="portraitTone" x1="0" y1="0" x2="0" y2="1">
      <stop offset="0" stop-color="#d9dde2"/>
      <stop offset="0.55" stop-color="#c9a48c"/>
      <stop offset="1" stop-color="#8e9aa8"/>
    </linearGradient>
  </defs>
  <polygon points="180,18 344,112 344,301 180,395 16,301 16,112" fill="url(#portraitTone)" role="img" aria-label="Portrait photograph of the chief executive"/>
</svg>
<h3 class="person-name">Marcus Hale</h3>
<p class="person-role">Chief Executive Officer</p>
<p class="person-bio">Lorem ipsum dolor sit amet, consectetur adipiscing elit, sed do eiusmod tempor incididunt ut labore et dolore magna aliqua. Ut enim ad minim veniam, quis nostrud exercitation ullamco laboris nisi ut aliquip ex ea commodo consequat. Duis aute irure dolor in reprehenderit in voluptate velit esse cillum dolore eu fugiat nulla pariatur. Excepteur sint occaecat cupidatat non proident, sunt in culpa qui officia deserunt mollit anim id est laborum. Duis aute irure dolor in reprehenderit in voluptate velit esse cillum dolore eu fugiat nulla pariatur. Excepteur sint occaecat cupidatat non proident, sunt in culpa qui officia deserunt mollit anim id est laborum.</p>

<div class="awards-band"></div>
<div class="trophy" role="img" aria-label="Silver trophy cup"></div>
<h2 class="section-title awards-title">OUR AWARDS</h2>
<svg class="award" style="left:103px" viewBox="0 0 180 202" role="img" aria-label="Award badge"><polygon points="90,0 180,50 180,152 90,202 0,152 0,50" fill="var(--orange)"/></svg>
<svg class="award" style="left:374px" viewBox="0 0 180 202" role="img" aria-label="Award badge"><polygon points="90,0 180,50 180,152 90,202 0,152 0,50" fill="var(--orange)"/></svg>
<svg class="award" style="left:644px" viewBox="0 0 180 202" role="img" aria-label="Award badge"><polygon points="90,0 180,50 180,152 90,202 0,152 0,50" fill="var(--orange)"/></svg>
<svg class="award" style="left:915px" viewBox="0 0 180 202" role="img" aria-label="Award badge"><polygon points="90,0 180,50 180,152 90,202 0,152 0,50" fill="var(--orange)"/></svg>

<footer>
  <div class="site-footer"></div>
  <p class="copyright">© 2015 - Veltra All Right Reserved</p>
  <a class="social-link" href="#" style="left:513px" aria-label="Social profile"></a>
  <a class="social-link" href="#" style="left:562px" aria-label="Social profile"></a>
  <a class="social-link" href="#" style="left:620px" aria-label="Social profile"></a>
  <a class="social-link" href="#" style="left:669px" aria-label="Social profile"></a>
  <svg class="back-to-top" viewBox="0 0 24 16" aria-label="Back to top">
    <polyline points="4,12 12,4 20,12" fill="none" stroke="#ffffff" stroke-width="2.5"/>
  </svg>
</footer>

</body>
</html>
```